CRPG is needing business cards, and stationary created.

Pixel Forge created a logo for our business, and now we are wanting business cards, and stationary. I have included two designs of the same logo. Please feel free to use them as you want. The name of the company is Cedar Ridge Property Group LLC, the address is 812 NE Tamber Ln., Suite 9, the city & state is Bend, Oregon, zip code is 97815, Telephone number is 541-237-4190, Fax number is 541-237-8856, the name on the business card is Travis Lundqor CMCA

Industry/Entity Type

Property Management

Contact Information for Business Card

The card needs to look professional. Upscale.

Requirements
Must have
• The colors we are using are on the logo that has been uploaded.

```html
<!DOCTYPE html>
<html lang="en">
<head>
<meta charset="utf-8">
<title>Cedar Ridge Property Group – Stationery</title>
<link href="https://fonts.googleapis.com/css2?family=Rubik:wght@300;400;500&display=swap" rel="stylesheet">
<style>
  :root{
    --backdrop:#36373a;
    --paper:#f2f2f4;
    --card:#ffffff;
    --teal:#1b8a72;
    --slate:#3e4a5a;
    --ink:#4a4d52;
    --rule:#6a6d72;
  }
  *{margin:0;padding:0;box-sizing:border-box}
  html,body{width:1200px;height:900px;overflow:hidden}
  body{background:var(--backdrop);font-family:"Rubik",sans-serif;position:relative;color:var(--ink)}

  .brand-name{font-family:"Rubik",sans-serif;font-weight:500;color:var(--teal);letter-spacing:.5px;white-space:nowrap}

  /* Letterhead */
  .letterhead{position:absolute;left:141px;top:100px;width:498px;height:704px;background:var(--paper);box-shadow:0 6px 18px rgba(0,0,0,.45)}
  .letterhead .brand{position:absolute;top:44px;left:0;width:100%;text-align:center}
  .letterhead .brand-name{font-size:27px}
  .letter-body{position:absolute;left:34px;right:34px;top:150px}
  .salutation{font-size:18px;font-weight:300;color:var(--ink);margin-bottom:16px}
  .letter-body p{font-size:9.6px;line-height:13px;font-weight:300;margin-bottom:16px;color:#5a5d62}
  .closing{position:absolute;left:34px;top:502px}
  .closing .regards{font-size:11.5px;color:var(--ink)}
  .signature{display:block;width:90px;height:16px;margin:8px 0 10px;background:linear-gradient(90deg,#c9cacd,#e3e4e6)}
  .signer{font-size:11.5px;color:var(--ink)}
  .signer-title{font-size:8.5px;color:var(--ink)}
  .signer-company{font-size:7px;font-weight:500;color:var(--ink);margin-top:6px;text-transform:uppercase}
  .letter-rule{position:absolute;left:34px;right:34px;top:612px;border-top:1px solid var(--rule)}

  .contacts{list-style:none;font-size:9.6px;color:var(--teal);line-height:12px}
  .contacts li{display:flex;align-items:center;gap:6px}
  .contacts svg{width:6px;height:6px;fill:var(--ink)}
  .address{font-size:9.6px;line-height:12.5px;color:var(--teal);text-align:right;letter-spacing:.3px}
  .letterhead .contacts{position:absolute;left:34px;top:629px}
  .letterhead .address{position:absolute;right:34px;top:652px}

  .footer-band{position:absolute;left:0;bottom:0;width:100%;display:block}

  /* Business card front */
  .card-front{position:absolute;left:700px;top:218px;width:358px;height:204px;background:var(--card);box-shadow:0 6px 16px rgba(0,0,0,.45)}
  .card-front .brand{position:absolute;left:15px;top:44px}
  .card-front .brand-name{font-size:19px}
  .holder{position:absolute;right:16px;top:82px;text-align:right}
  .holder-name{font-size:14.5px;letter-spacing:.6px;color:#2c2f33;text-transform:uppercase}
  .holder-cred{font-size:8px;color:var(--teal);margin-top:2px}
  .card-rule{position:absolute;left:15px;right:16px;top:120px;border-top:1px solid var(--rule)}
  .card-front .contacts{position:absolute;left:15px;top:136px;font-size:9px}
  .card-front .address{position:absolute;right:16px;top:162px;font-size:9px}

  /* Business card back */
  .card-back{position:absolute;left:702px;top:482px;width:356px;height:204px;background:var(--slate);box-shadow:0 6px 16px rgba(0,0,0,.45)}
  .card-back .pattern{position:absolute;inset:0;background:linear-gradient(135deg,#435064,#3a4556)}
  .card-back .brand{position:absolute;left:56px;top:95px;display:flex;align-items:center;gap:7px}
  .card-back .brand-mark{width:10px;height:10px;border-radius:50%;background:#fff}
  .card-back .brand-name{font-size:15px;color:#fff}
</style>
</head>
<body>

<article class="letterhead">
  <header class="brand"><span class="brand-name">CEDAR RIDGE</span></header>

  <section class="letter-body">
    <h2 class="salutation">Dear Sir</h2>
    <p>Lorem ipsum dolor sit amet, an vel recteque dissentiet, detracto albucius platonem ex vel, eros repudiandae cu. Atqui aliquando nec an, unum graece adolescens vel ad. Id odio scae has, iudico euismod atomorum ius ea, cum ea honestatis quaerendum theophrastus. Mea honestatis quaerendum theophrastus. Mea</p>
    <p>Lorem ipsum dolor sit amet, an vel recteque dissentiet, detracto albucius platonem ex vel, eros repudiandae cu. Atqui aliquando nec an, unum graece adolescens vel ad. Id odio scae has, iudico euismod atomorum ius ea, cum ea honestatis quaerendum theophrastus. Mea doming repudiandae ex, cu cum civibus assentior posidonium. Quo etiam pertinax ex, te eros repudiandae cu. Atqui aliquando nec an, unum graece adolescens vel ad. Id odio scae honestatis quaerendum theophrastus. Mea</p>
    <p>Lorem ipsum dolor sit amet, an vel recteque dissentiet, detracto albucius platonem ex vel, eros repudiandae cu. Atqui aliquando nec an, unum graece adolescens vel ad. Id odio scae has, iudico euismod atomorum ius ea, cum ea honestatis quaerendum theophrastus. Mea honestatis quaerendum theophrastus. Mea</p>
    <p>Lorem ipsum dolor sit amet, an vel recteque dissentiet, detracto albucius platonem ex vel, eros repudiandae cu. Atqui aliquando nec an, unum graece adolescens vel ad. Id odio scae has, iudico euismod atomorum ius ea, cum ea honestatis quaerendum theophrastus. Mea honestatis quaerendum theophrastus. Mea</p>
  </section>

  <section class="closing">
    <div class="regards">Kind Regards</div>
    <span class="signature" role="img" aria-label="Handwritten signature of Warren Halvik"></span>
    <div class="signer">Warren Halvik</div>
    <div class="signer-title">Chief Alchemist</div>
    <div class="signer-company">Northvale Corporate Holdings LTD</div>
  </section>

  <div class="letter-rule"></div>

  <ul class="contacts">
    <li><svg viewBox="0 0 10 10"><path d="M2 0h2l1 3-1.5 1a6 6 0 0 0 2.5 2.5L7 5l3 1v2a2 2 0 0 1-2 2A8 8 0 0 1 0 2a2 2 0 0 1 2-2z"/></svg>541-237-4190</li>
    <li><svg viewBox="0 0 10 10"><rect x="2" y="0" width="6" height="3"/><rect x="0" y="3" width="10" height="5" rx="1"/><rect x="2" y="7" width="6" height="3"/></svg>541-237-8856</li>
    <li><svg viewBox="0 0 10 10"><path d="M0 2h10v6H0z M1 3l4 3 4-3" fill="none" stroke="#4a4d52" stroke-width="1"/></svg>info@crpgllc.com</li>
    <li><svg viewBox="0 0 10 10"><circle cx="5" cy="5" r="4.2" fill="none" stroke="#4a4d52" stroke-width="1.2"/><path d="M1 5h8M5 1v8" stroke="#4a4d52" stroke-width="1"/></svg>www.crpgllc.com</li>
  </ul>
  <address class="address">812 NE Tamber Ln., Suite 9,<br>Bend, Oregon, 97815</address>

  <svg class="footer-band" viewBox="0 0 498 22" width="498" height="22" preserveAspectRatio="none">
    <path d="M0 4 H285 Q300 4 306 9 H0 Z" fill="var(--teal)"/>
    <path d="M0 10 H300 Q330 0 360 0 H498 V22 H0 Z" fill="var(--slate)"/>
  </svg>
</article>

<article class="card-front">
  <div class="brand"><span class="brand-name">CEDAR RIDGE</span></div>
  <div class="holder">
    <div class="holder-name">Travis Lundqor</div>
    <div class="holder-cred">CMCA</div>
  </div>
  <div class="card-rule"></div>
  <ul class="contacts">
    <li><svg viewBox="0 0 10 10"><path d="M2 0h2l1 3-1.5 1a6 6 0 0 0 2.5 2.5L7 5l3 1v2a2 2 0 0 1-2 2A8 8 0 0 1 0 2a2 2 0 0 1 2-2z"/></svg>541-237-4190</li>
    <li><svg viewBox="0 0 10 10"><rect x="2" y="0" width="6" height="3"/><rect x="0" y="3" width="10" height="5" rx="1"/><rect x="2" y="7" width="6" height="3"/></svg>541-237-8856</li>
    <li><svg viewBox="0 0 10 10"><path d="M0 2h10v6H0z M1 3l4 3 4-3" fill="none" stroke="#4a4d52" stroke-width="1"/></svg>info@crpgllc.com</li>
    <li><svg viewBox="0 0 10 10"><circle cx="5" cy="5" r="4.2" fill="none" stroke="#4a4d52" stroke-width="1.2"/><path d="M1 5h8M5 1v8" stroke="#4a4d52" stroke-width="1"/></svg>www.crpgllc.com</li>
  </ul>
  <address class="address">812 NE Tamber Ln., Suite 9,<br>Bend, Oregon, 97815</address>
  <svg class="footer-band" viewBox="0 0 358 15" width="358" height="15" preserveAspectRatio="none">
    <path d="M0 2 H200 Q212 2 216 6 H0 Z" fill="var(--teal)"/>
    <path d="M0 7 H210 Q235 0 260 0 H358 V15 H0 Z" fill="var(--slate)"/>
  </svg>
</article>

<article class="card-back">
  <div class="pattern" role="img" aria-label="Subtle repeating geometric pattern in slate tones"></div>
  <div class="brand"><span class="brand-mark"></span><span class="brand-name">CEDAR RIDGE</span></div>
</article>

</body>
</html>
```